Game, Voice & Dedicated Server Company Needs a Business Card Design

We need a new business card design, centered around our new logo (PSD provided below).

Designs that we do like:
https://pixelmarsh.net/item/corporate-business-card/5382017?s_rank=43 (needs to be made more eye catching)

Our main areas of business are:
- Dedicated Servers
- Game Servers
- Voice Servers
- Mitigation Security Specialists

Industry/Entity Type

Business

Contact Information for Business Card

On the card: (and anything else you would suggest)
- Staff member name
- Staff member position in company
- Staff member phone number
- Staff member email
- Other / Staff member Skype
- Website link

Colors
9bcb3c
abd036

Requirements
Must have
• Design of Card:
• - Green (same green as the logo)
• - Business / Corporate design
• - Something a little different / abstract that shouts premium

```html
<!DOCTYPE html>
<html lang="en">
<head>
<meta charset="utf-8">
<title>Brightpath Hosting – Business Card</title>
<link rel="stylesheet" href="https://fonts.googleapis.com/css2?family=Montserrat:wght@400;500;700;800&display=swap">
<style>
  :root {
    --stage: #2b2b2b;
    --card: #050505;
    --green: #9bcb3c;
    --green-deep: #6fa72c;
    --grey: #8e8f91;
    --grey-light: #b9babc;
    --white: #f2f2f2;
  }
  * { margin: 0; padding: 0; box-sizing: border-box; }
  html, body { width: 1200px; height: 900px; overflow: hidden; }
  body {
    background: var(--stage);
    font-family: "Montserrat", Arial, sans-serif;
    position: relative;
  }
  .card {
    position: absolute;
    width: 560px;
    height: 320px;
    background: var(--card);
    box-shadow: 0 14px 30px rgba(0,0,0,.55);
    overflow: hidden;
  }
  .card--front { left: 90px; top: 110px; }
  .card--back { left: 550px; top: 470px; }

  .wordmark {
    color: var(--green);
    font-weight: 800;
    text-transform: uppercase;
    line-height: .95;
    letter-spacing: -0.5px;
    display: flex;
    align-items: center;
    gap: 14px;
  }
  .wordmark__square {
    width: 44px; height: 44px;
    background: var(--green);
    flex: none;
  }
  .card--front .wordmark {
    position: absolute;
    left: 120px; top: 118px;
    font-size: 34px;
  }
  .card--front .website {
    position: absolute;
    left: 0; right: 0; bottom: 34px;
    text-align: center;
    font-size: 13px;
    color: var(--grey-light);
    letter-spacing: .3px;
  }
  .website .domain { color: var(--green); }

  .side-band {
    position: absolute;
    left: 0; top: 0; bottom: 0;
    width: 28px;
    background: linear-gradient(180deg, var(--green) 0%, var(--grey) 30%, var(--green-deep) 55%, var(--grey-light) 78%, var(--green) 100%);
  }
  .card--back .wordmark {
    position: absolute;
    left: 52px; top: 30px;
    font-size: 30px;
  }
  .decor-block {
    position: absolute;
    right: 40px; top: 30px;
    width: 150px; height: 150px;
    background: linear-gradient(90deg, var(--green) 0 50%, var(--grey) 50% 100%);
  }
  .staff {
    position: absolute;
    left: 52px; top: 120px;
  }
  .staff__name {
    color: var(--green);
    font-weight: 700;
    font-size: 21px;
  }
  .staff__role {
    color: var(--white);
    font-size: 12px;
    margin-top: 2px;
  }
  .contact {
    list-style: none;
    position: absolute;
    left: 52px; top: 184px;
    color: var(--white);
    font-size: 13px;
    line-height: 19px;
  }
  .contact li { display: flex; align-items: center; gap: 8px; }
  .contact svg { width: 11px; height: 11px; flex: none; }
  .services {
    position: absolute;
    left: 70px; top: 268px;
    color: var(--white);
    font-size: 13px;
    line-height: 18px;
  }
  .services .sep { color: var(--green); }
</style>
</head>
<body>

<section class="card card--front">
  <div class="wordmark"><span class="wordmark__square"></span><span>Brightpath<br>Hosting</span></div>
  <p class="website">www.<span class="domain">brightpathhosting</span>.com</p>
</section>

<section class="card card--back">
  <div class="side-band" role="img" aria-label="Faceted green and grey triangle band"></div>
  <div class="wordmark"><span>Brightpath<br>Hosting</span></div>
  <div class="decor-block"></div>

  <div class="staff">
    <p class="staff__name">Marten Olsen</p>
    <p class="staff__role">Director</p>
  </div>

  <ul class="contact">
    <li>
      <svg viewBox="0 0 12 12"><path d="M2 1h3l1 3-1.5 1a6 6 0 0 0 2.5 2.5L8 6l3 1v3a1 1 0 0 1-1 1A9 9 0 0 1 1 2a1 1 0 0 1 1-1z" fill="#9bcb3c"/></svg>
      +330 2460-1358
    </li>
    <li>
      <svg viewBox="0 0 12 12"><rect x="1" y="2.5" width="10" height="7" fill="none" stroke="#9bcb3c" stroke-width="1.3"/><path d="M1 2.5l5 4 5-4" fill="none" stroke="#9bcb3c" stroke-width="1.3"/></svg>
      info@brightpathhosting.com
    </li>
    <li>
      <svg viewBox="0 0 12 12"><circle cx="6" cy="6" r="5" fill="#9bcb3c"/></svg>
      @brightpathhosting
    </li>
    <li>
      <svg viewBox="0 0 12 12"><g fill="none" stroke="#9bcb3c" stroke-width="1.1"><circle cx="6" cy="6" r="5"/><ellipse cx="6" cy="6" rx="2.2" ry="5"/><path d="M1 6h10"/></g></svg>
      www.<span style="color:var(--green)">brightpathhosting</span>.com
    </li>
  </ul>

  <div class="services">
    <p>Dedicated Servers <span class="sep">-</span> Game Servers</p>
    <p>Voice Servers <span class="sep">-</span> Business relations</p>
  </div>
</section>

</body>
</html>
```